Brightmere Facebook Design

Build out a really nice and professional Facebook Page and full banner for Brightmere perhaps with the our services portfolio across the page as well,
Pls check www.brightmere-example.com.au for ideas to a make the Facebook Page look professional like a similar theme to our website and the porfolio of services

Main photo please emphasis the equipment cleaning and the gurney cleaning a lower priority to emphasize is the general cleaning
Thanks very much

Target Market(s)

Restaurant, warehouses, factories, car and fleet companies, hotels and buffets, chain restaurants, pizza huts, burger eateries, leisure centres

Industry/Entity Type

Cleaning Services

Font styles to use
Serif

Colors
3277b5
f04a50
f37122
fcf299
ec1f27

Requirements
Must have
• Energy and professional Facebook Site with some of the Brightmere Flowers across it and the portfolio of services
Nice to have
• Good vibrant colours

Professional similar to the website

```html
<!DOCTYPE html>
<html lang="en">
<head>
<meta charset="utf-8">
<title>Brightmere Facebook Design</title>
<link rel="stylesheet" href="https://fonts.googleapis.com/css2?family=Merriweather:wght@400;700&display=swap">
<style>
  :root {
    --brand-blue: #1b3f74;
    --brand-blue-deep: #163563;
    --brand-blue-light: #3277b5;
    --brand-orange: #f37122;
    --brand-orange-soft: #f7a06a;
    --brand-red: #ec1f27;
    --canvas-bg: #f3f5f8;
    --flower-tint: #e6ebf2;
    --text-dark: #1c3560;
    --white: #ffffff;
  }
  * { box-sizing: border-box; margin: 0; padding: 0; }
  html, body { width: 1200px; height: 444px; overflow: hidden; background: var(--canvas-bg); }
  body { font-family: "Merriweather", Georgia, serif; }

  .cover {
    position: relative;
    width: 1200px;
    height: 444px;
    overflow: hidden;
    background:
      radial-gradient(circle at 720px 420px, var(--flower-tint) 0 70px, transparent 71px),
      radial-gradient(circle at 1120px 150px, var(--flower-tint) 0 90px, transparent 91px),
      radial-gradient(circle at 40px 200px, var(--flower-tint) 0 80px, transparent 81px),
      var(--canvas-bg);
  }

  /* Service tiles: slanted, rounded panels */
  .service-tile {
    position: absolute;
    transform: skewX(-7deg);
    border-radius: 16px;
    overflow: hidden;
    box-shadow: 0 3px 10px rgba(20, 40, 80, 0.18);
  }
  .service-photo {
    position: absolute;
    inset: 0;
  }
  .service-label {
    position: absolute;
    color: var(--white);
    font-weight: 700;
    line-height: 1.25;
  }
  .service-label span { display: block; transform: skewX(7deg); }

  .tile-equipment { left: 28px; top: -16px; width: 336px; height: 338px; }
  .tile-equipment .service-photo { background: linear-gradient(160deg, #5b4a3c 0%, #9a8f86 40%, #c9c6c2 70%, #6f6a66 100%); }
  .tile-equipment .service-label {
    left: 0; right: 0; bottom: 0; height: 102px;
    background: var(--brand-blue);
    font-size: 25px; padding: 38px 0 0 36px;
  }

  .tile-kitchen { left: 338px; top: 11px; width: 268px; height: 354px; }
  .tile-kitchen .service-photo { background: linear-gradient(170deg, #b9bcbf 0%, #e0e2e3 35%, #8f9497 65%, #4a5054 100%); }
  .tile-kitchen .service-label {
    left: 0; right: 0; bottom: 0; height: 104px;
    background: var(--brand-blue);
    font-size: 22px; padding: 22px 0 0 30px;
  }

  .tile-gurney { left: 594px; top: 59px; width: 270px; height: 171px; }
  .tile-gurney .service-photo { background: linear-gradient(120deg, #6d7a86 0%, #aab4bc 45%, #4d5a66 100%); }
  .tile-gurney .service-label {
    top: 0; right: 0; bottom: 0; width: 160px;
    background: rgba(27, 63, 116, 0.92);
    font-size: 19px; padding: 38px 0 0 20px;
  }

  .tile-office { left: 566px; top: 243px; width: 276px; height: 174px; }
  .tile-office .service-photo { background: linear-gradient(110deg, #cfd3d6 0%, #f0f1f2 45%, #b9bec2 100%); }
  .tile-office .service-label {
    top: 26px; left: 0; right: 0; height: 74px;
    background: rgba(27, 63, 116, 0.92);
    font-size: 18px; padding: 13px 0 0 96px;
  }

  /* Right column */
  .link-tab {
    position: absolute;
    left: 884px;
    width: 316px;
    height: 44px;
    background: linear-gradient(90deg, var(--brand-orange) 0%, var(--brand-orange) 60%, var(--brand-orange-soft) 100%);
    color: var(--white);
    font-weight: 700;
    font-size: 19px;
    padding: 10px 0 0 32px;
  }
  .tab-careers { top: 35px; }
  .tab-stories { top: 89px; }

  .client-name {
    position: absolute;
    left: 906px;
    top: 160px;
    display: flex;
    align-items: center;
    gap: 12px;
    color: var(--brand-red);
    font-weight: 700;
    font-size: 24px;
  }
  .client-name .mark {
    width: 56px; height: 56px;
    border-radius: 50%;
    background: var(--brand-red);
  }

  .success-story {
    position: absolute;
    left: 894px;
    top: 250px;
    width: 232px;
    color: var(--text-dark);
    font-size: 15px;
    line-height: 1.5;
  }

  .panel-code {
    position: absolute;
    left: 1150px;
    top: 408px;
    font-size: 11px;
    color: var(--text-dark);
  }

  /* Company name */
  .brand {
    position: absolute;
    left: 44px;
    top: 362px;
    display: flex;
    align-items: center;
    gap: 12px;
    color: var(--brand-orange);
    font-weight: 400;
    font-size: 36px;
  }
  .brand .mark {
    width: 44px; height: 44px;
    border-radius: 50%;
    background: var(--brand-blue-light);
  }
</style>
</head>
<body>
  <main class="cover">
    <section class="service-tile tile-equipment">
      <div class="service-photo" role="img" aria-label="Photo of a commercial soft-serve and sundae machine in a restaurant kitchen"></div>
      <div class="service-label"><span>Equipment Services</span></div>
    </section>

    <section class="service-tile tile-kitchen">
      <div class="service-photo" role="img" aria-label="Photo of a clean stainless steel commercial kitchen with heat lamps"></div>
      <div class="service-label"><span>Kitchen Detail<br>Clean</span></div>
    </section>

    <section class="service-tile tile-gurney">
      <div class="service-photo" role="img" aria-label="Photo of a worker pressure washing paving"></div>
      <div class="service-label"><span>Gurney High<br>Pressure<br>Cleaning</span></div>
    </section>

    <section class="service-tile tile-office">
      <div class="service-photo" role="img" aria-label="Photo of a bright, tidy office interior with a potted plant"></div>
      <div class="service-label"><span>General Office<br>Cleaning</span></div>
    </section>

    <div class="link-tab tab-careers">Careers information</div>
    <div class="link-tab tab-stories">Our Success Stories</div>

    <div class="client-name"><span class="mark"></span>Crestline Chicken</div>

    <p class="success-story">We successfully managed the roll out of 200 Equipment Asset Frost Whirl Machines, 191 Vellano Machines for Crestline Chicken from 2012 to 2019 for the facilities department.</p>

    <div class="panel-code">M1</div>

    <div class="brand"><span class="mark"></span>Brightmere</div>
  </main>
</body>
</html>
```